CBD AgriBusiness Cannabis Cup Business Card

We are HiTec producer of medical cannabis CBD Switzerland of high quality. Our website is alpinleafo.com, we will also revisit it graphically, the winner of this contest will be the graphic designer chosen for the new design of the website. We stand out by the skill of the team, many of our engineers we win cup cannabis. I join the current map to take as an example but to revisit completely: deletion of surname and first name, modification of funds (front / back), reorganization of text info, highlighting the address of the website. three characteristics define the business card: Professional, Class, refined. The business card must be optimized for soft-touch and selective varnish printing.

Target Market(s)

Customers and Suppliers

Industry/Entity Type

Agribusiness

Contact Information for Business Card

Logo, Tél / Whatsapp, mail, url du site : alpinleafo.com

Font styles to use
Sans Serif

Requirements
Must have
• Logo of alpinleafo.com
Nice to have
• a design that stands out well on the selective varnish
Should not have
• Last name and first name

```html
<!DOCTYPE html>
<html lang="en">
<head>
<meta charset="utf-8">
<title>alpinleafo business card</title>
<link href="https://fonts.googleapis.com/css2?family=Montserrat:wght@400;500;600;800&display=swap" rel="stylesheet">
<style>
  :root {
    --backdrop: #9c9c9c;
    --card-dark: #0f1210;
    --card-dark-edge: #1c211d;
    --card-light: #ffffff;
    --leaf-green: #7cc04b;
    --leaf-deep: #3c4a22;
    --text-grey: #555a5c;
    --logo-grey: #4a4d50;
    --white: #ffffff;
  }
  * { box-sizing: border-box; margin: 0; padding: 0; }
  html, body {
    width: 1200px; height: 930px; overflow: hidden;
    background: var(--backdrop);
    font-family: "Montserrat", sans-serif;
  }
  .canvas { position: relative; width: 1200px; height: 930px; }

  .card {
    position: absolute;
    width: 630px; height: 360px;
    border-radius: 26px;
    overflow: hidden;
    box-shadow: 0 10px 24px rgba(0,0,0,0.25);
  }

  /* Front */
  .card--front {
    left: 100px; top: 90px;
    background: linear-gradient(120deg, var(--card-dark-edge) 0%, var(--card-dark) 55%, #050605 100%);
  }
  .card--front .foliage {
    position: absolute; right: 0; top: 0;
    width: 300px; height: 260px;
    background: radial-gradient(ellipse at 70% 35%, #6f7d3a 0%, var(--leaf-deep) 40%, rgba(15,18,16,0) 75%);
  }
  .card--front .brand {
    position: absolute; left: 150px; top: 190px;
    display: flex; align-items: center; gap: 14px;
  }
  .brand__mark {
    width: 30px; height: 30px; background: var(--leaf-green);
  }
  .brand__name {
    font-weight: 800; font-size: 58px; letter-spacing: -1px; line-height: 1;
  }
  .card--front .brand__name { color: var(--white); }

  /* Back */
  .card--back {
    left: 470px; top: 480px;
    background: var(--card-light);
  }
  .card--back .brand {
    position: absolute; left: 40px; top: 218px;
    display: flex; align-items: center; gap: 10px;
  }
  .card--back .brand__mark { width: 24px; height: 24px; }
  .card--back .brand__name { color: var(--logo-grey); font-size: 48px; }

  .divider {
    position: absolute; left: 360px; top: 90px;
    width: 2px; height: 180px; background: var(--leaf-green);
  }
  .contact {
    position: absolute; left: 384px; top: 100px;
    color: var(--text-grey); font-size: 13px; line-height: 1.45;
  }
  .contact__role {
    color: var(--leaf-green); font-weight: 600; font-size: 15px;
    letter-spacing: 0.5px; margin-bottom: 12px;
  }
  .contact__address { margin-bottom: 12px; }
  .contact__line { display: flex; align-items: center; gap: 8px; }
  .contact__line svg { width: 11px; height: 11px; flex: none; }
  .contact__web strong { color: var(--leaf-green); font-weight: 600; }
</style>
</head>
<body>
<div class="canvas">

  <section class="card card--front">
    <div class="foliage" role="img" aria-label="Photograph of green cannabis leaves fading into the dark background"></div>
    <div class="brand">
      <span class="brand__mark"></span>
      <span class="brand__name">alpinleafo</span>
    </div>
  </section>

  <section class="card card--back">
    <div class="brand">
      <span class="brand__mark"></span>
      <span class="brand__name">alpinleafo</span>
    </div>
    <div class="divider"></div>
    <div class="contact">
      <p class="contact__role">DIRECTOR</p>
      <p class="contact__address">42b Harbour Lane,<br>Lakeview, NZ, 8042</p>
      <p class="contact__line">
        <svg viewBox="0 0 12 12"><path d="M3 1 L5 3.5 L4 5 Q5 7 7 8 L8.5 7 L11 9 L9.5 11 Q4 10.5 1 3 Z" fill="#7cc04b"/></svg>
        +41 (0) 79 555 01 23
      </p>
      <p class="contact__line">
        <svg viewBox="0 0 12 12"><rect x="3" y="0.5" width="6" height="11" rx="1.2" fill="none" stroke="#7cc04b" stroke-width="1.2"/><circle cx="6" cy="9.5" r="0.7" fill="#7cc04b"/></svg>
        +44 7700 90 01 24
      </p>
      <p class="contact__line">
        <svg viewBox="0 0 12 12"><rect x="0.8" y="2.5" width="10.4" height="7" fill="none" stroke="#7cc04b" stroke-width="1.2"/><path d="M1 3 L6 7 L11 3" fill="none" stroke="#7cc04b" stroke-width="1.2"/></svg>
        office@alpinleafo.com
      </p>
      <p class="contact__line contact__web">
        <svg viewBox="0 0 12 12"><circle cx="6" cy="6" r="5" fill="none" stroke="#7cc04b" stroke-width="1.2"/><ellipse cx="6" cy="6" rx="2.2" ry="5" fill="none" stroke="#7cc04b" stroke-width="1"/><path d="M1 6 H11" stroke="#7cc04b" stroke-width="1"/></svg>
        <span>www.<strong>alpinleafo</strong>.com</span>
      </p>
    </div>
  </section>

</div>
</body>
</html>
```